Full service meeting planning company needs new business cards

Velmora Linkway is a full service meeting planning company that specializes in on-line conference registration web development and event communications. We combine citywide hotel management, mobile applications, eblast reminders, confirmation letters, and customized reporting to create a seamless registration process. We also manage group motor coach transportation, food and beverages, entertainment, stage and lighting for group of 10 to 4000.

Target Market(s)

Corporations and associations

Industry/Entity Type

Event Planning

Contact Information for Business Card

standard size 3.5" wide and 2" tall

Font styles to use
Serif
Sans Serif

Colors
f37122
f78f20
333333
5c5c5c
9d9d9d
f68d4d

Requirements
Must have
• {name}
• Velmora Linkway
• P.O. Box 7384, Grand Rapids, M I 49568
• www.velmoralinkway.com
• {email}
• {phone}
• {mobile phone}
Nice to have
• Our colors are black, grey and orange as an accent color
Should not have
• I am not happy with our website layout anymore either. It feels dark and old but it does explain who we are pretty well if you'd like to review; www.velmoralinkway.com

```html
<!DOCTYPE html>
<html lang="en">
<head>
<meta charset="utf-8">
<title>Velmora Linkway – Business Card</title>
<link href="https://fonts.googleapis.com/css2?family=Lato:wght@400;700&display=swap" rel="stylesheet">
<style>
  :root {
    --orange: #ea8434;
    --white: #ffffff;
    --grey: #9d9d9d;
    --backdrop: #3d3d3d;
  }
  * { margin: 0; padding: 0; box-sizing: border-box; }
  html, body { width: 1200px; height: 810px; overflow: hidden; }
  body {
    background: var(--backdrop);
    font-family: "Lato", sans-serif;
    position: relative;
  }
  .card {
    position: absolute;
    width: 560px;
    height: 320px;
    overflow: hidden;
  }
  .card-front {
    left: 90px; top: 80px;
    background: var(--orange);
    color: var(--white);
    display: flex;
    flex-direction: column;
    align-items: center;
    justify-content: center;
  }
  .front-mark {
    width: 110px; height: 110px;
    border-radius: 50%;
    background: var(--white);
  }
  .front-name {
    margin-top: 22px;
    font-size: 26px;
    font-weight: 700;
    letter-spacing: 2px;
    text-transform: uppercase;
  }
  .front-web {
    margin-top: 28px;
    font-size: 13px;
    letter-spacing: 0.3px;
  }
  .card-back { left: 550px; top: 420px; }
  .back-shape { position: absolute; inset: 0; }
  .brand {
    position: absolute;
    left: 24px; top: 112px;
    width: 290px;
    display: flex;
    flex-direction: column;
    align-items: center;
    gap: 14px;
  }
  .brand-dot {
    width: 50px; height: 50px;
    border-radius: 50%;
    background: var(--orange);
  }
  .brand-name {
    color: var(--orange);
    font-size: 22px;
    font-weight: 700;
    letter-spacing: 1.5px;
    text-transform: uppercase;
    white-space: nowrap;
  }
  .details {
    position: absolute;
    right: 24px; top: 22px;
    text-align: right;
    color: var(--white);
  }
  .person-name { font-size: 20px; font-weight: 400; }
  .person-title { font-size: 12px; margin-top: 2px; }
  .address { margin-top: 40px; font-size: 12px; line-height: 1.45; }
  .contacts { margin-top: 14px; font-size: 12px; line-height: 1.6; list-style: none; }
  .contacts li { display: flex; justify-content: flex-end; align-items: center; gap: 6px; }
  .contacts svg { width: 11px; height: 11px; fill: var(--white); flex: none; }
</style>
</head>
<body>
  <section class="card card-front">
    <div class="front-mark"></div>
    <div class="front-name">Velmora Linkway</div>
    <div class="front-web">www.velmoralinkway.com</div>
  </section>

  <section class="card card-back">
    <svg class="back-shape" viewBox="0 0 560 320" width="560" height="320">
      <rect width="560" height="320" fill="var(--orange)"/>
      <path d="M0 0 H150 Q385 70 378 320 H0 Z" fill="var(--grey)"/>
      <path d="M0 0 H140 Q370 70 362 320 H0 Z" fill="var(--white)"/>
    </svg>

    <div class="brand">
      <div class="brand-dot"></div>
      <div class="brand-name">Velmora Linkway</div>
    </div>

    <div class="details">
      <div class="person-name">Marissa Dorlund, CMP</div>
      <div class="person-title">Sr. Project Manager</div>
      <div class="address">
        Velmora Linkway<br>
        P.O. Box 7384<br>
        Grand Rapids, M I 49568
      </div>
      <ul class="contacts">
        <li>616 555 0142 x11
          <svg viewBox="0 0 24 24"><path d="M6.6 10.8a15 15 0 0 0 6.6 6.6l2.2-2.2a1 1 0 0 1 1-.25 11.4 11.4 0 0 0 3.6.57 1 1 0 0 1 1 1V20a1 1 0 0 1-1 1A17 17 0 0 1 3 4a1 1 0 0 1 1-1h3.5a1 1 0 0 1 1 1c0 1.25.2 2.45.57 3.6a1 1 0 0 1-.25 1z"/></svg>
        </li>
        <li>616 555 0187
          <svg viewBox="0 0 24 24"><path d="M7 1h10a2 2 0 0 1 2 2v18a2 2 0 0 1-2 2H7a2 2 0 0 1-2-2V3a2 2 0 0 1 2-2zm0 3v15h10V4z"/></svg>
        </li>
        <li>info@velmoralinkway.com
          <svg viewBox="0 0 24 24"><path d="M2 5h20v14H2zm2 2v.4l8 5 8-5V7l-8 5z"/></svg>
        </li>
        <li>www.velmoralinkway.com
          <svg viewBox="0 0 24 24"><path d="M12 2a10 10 0 1 0 0 20 10 10 0 0 0 0-20zm0 2c1.5 1.8 2.4 4.4 2.5 7h-5c.1-2.6 1-5.2 2.5-7zM4.1 11a8 8 0 0 1 3.6-6 14 14 0 0 0-1.2 6zm0 2h2.4a14 14 0 0 0 1.2 6 8 8 0 0 1-3.6-6zm7.9 7c-1.5-1.8-2.4-4.4-2.5-7h5c-.1 2.6-1 5.2-2.5 7zm4.3-1a14 14 0 0 0 1.2-6h2.4a8 8 0 0 1-3.6 6zm1.2-8a14 14 0 0 0-1.2-6 8 8 0 0 1 3.6 6z"/></svg>
        </li>
      </ul>
    </div>
  </section>
</body>
</html>
```